business card double side design

We need a business card design for our company PLUMlearnhub. DOUBLE SIDED. We provide continuing education programs & courses across North America. Our website is www.plumlearnhub.example - please use the grey pinstrip concept as part of the design. Compliment the branding that is occuring on that site!
Please use pantones daa520 and 3f3151. Verdana for text. I have attached our logo.
I would like the logo & website address www.PLUMlearnhub.example on the front of the card, all other info on the backside. The final design should communicate authority and credibility.

• verdanda

• pantones daa520 and 3f3151. Verdana for text.
• must compliment the branding occuring on the www.PLUMlearnhub.example

```html
<!DOCTYPE html>
<html lang="en">
<head>
<meta charset="utf-8">
<title>PLUMlearnhub business card</title>
<link rel="stylesheet" href="https://fonts.googleapis.com/css2?family=Open+Sans:wght@400;600;700&family=Quicksand:wght@700&display=swap">
<style>
  :root {
    --plum: #3f3151;
    --gold: #daa520;
    --paper: #f5f5f5;
    --ink: #1e1e1e;
    --backdrop: #cdcdcd;
  }
  * { box-sizing: border-box; margin: 0; padding: 0; }
  html, body { width: 1200px; height: 1005px; overflow: hidden; }
  body {
    background: var(--backdrop);
    font-family: "Open Sans", Verdana, sans-serif;
    color: var(--ink);
    position: relative;
  }
  .card {
    position: absolute;
    left: 250px;
    width: 700px;
    height: 400px;
    background: var(--paper);
    overflow: hidden;
    box-shadow: 0 6px 16px rgba(0,0,0,0.18);
  }
  .card--front { top: 70px; }
  .card--back { top: 535px; }

  /* brand lockup */
  .brand { position: absolute; display: flex; align-items: center; gap: 20px; }
  .brand__seal {
    border-radius: 50%;
    background: radial-gradient(circle at 40% 35%, #f0c44a, var(--gold) 60%, #a97a10);
    flex: none;
  }
  .brand__name {
    font-family: "Open Sans", Verdana, sans-serif;
    font-weight: 700;
    color: var(--plum);
    letter-spacing: 0.5px;
  }
  .card--front .brand { left: 160px; top: 115px; }
  .card--front .brand__seal { width: 130px; height: 130px; }
  .card--front .brand__name { font-size: 44px; }

  .front__web {
    position: absolute;
    left: 0; right: 0; top: 302px;
    display: flex; align-items: center; justify-content: center; gap: 14px;
    font-size: 17px; color: var(--ink);
  }
  .front__dash { width: 48px; height: 3px; background: var(--plum); transform: skewY(-4deg); }
  .front__band {
    position: absolute; left: 0; right: 0; bottom: 0; height: 44px;
    background: var(--plum);
    border-top: 4px solid var(--gold);
  }

  /* back */
  .back__rail {
    position: absolute; left: 0; top: 0; bottom: 0; width: 62px;
    background: var(--plum);
    border-right: 5px solid var(--gold);
  }
  .card--back .brand { left: 120px; top: 40px; }
  .card--back .brand__seal { width: 108px; height: 108px; }
  .card--back .brand__name { font-size: 34px; }
  .back__social { position: absolute; right: 42px; top: 44px; display: flex; gap: 6px; }
  .back__social span { width: 26px; height: 26px; background: var(--plum); border-radius: 3px; }
  .holder { position: absolute; left: 110px; top: 190px; }
  .holder__name { font-family: "Quicksand", Verdana, sans-serif; font-size: 27px; color: var(--plum); }
  .holder__role { font-size: 15px; margin-top: 2px; }
  .contact { position: absolute; left: 114px; top: 278px; list-style: none; }
  .contact li { display: flex; align-items: center; gap: 14px; font-size: 16px; line-height: 25px; }
  .contact svg { width: 16px; height: 16px; fill: var(--gold); flex: none; }
</style>
</head>
<body>
  <section class="card card--front" aria-label="Card front">
    <div class="brand">
      <div class="brand__seal"></div>
      <div class="brand__name">PLUMlearnhub</div>
    </div>
    <div class="front__web">
      <span class="front__dash"></span>
      <span>www.PLUMlearnhub.example</span>
      <span class="front__dash"></span>
    </div>
    <div class="front__band"></div>
  </section>

  <section class="card card--back" aria-label="Card back">
    <div class="back__rail"></div>
    <div class="brand">
      <div class="brand__seal"></div>
      <div class="brand__name">PLUMlearnhub</div>
    </div>
    <div class="back__social" aria-label="Social profiles"><span></span><span></span><span></span></div>
    <div class="holder">
      <div class="holder__name">Lena Marsh</div>
      <div class="holder__role">Technical Support</div>
    </div>
    <ul class="contact">
      <li><svg viewBox="0 0 16 16"><path d="M2 6c0-2 2-3 6-3s6 1 6 3l-3 1-1-2H6L5 7zM4 8h8l1 6H3z"/></svg>555.014.2290</li>
      <li><svg viewBox="0 0 16 16"><path d="M1 3h14v10H1zM2 4l6 5 6-5v1L8 10 2 5z"/></svg>lena@PLUMlearnhub.example</li>
      <li><svg viewBox="0 0 16 16"><path d="M8 1a7 7 0 1 0 0 14A7 7 0 0 0 8 1zm0 1.2c.9 0 1.9 2 2.1 5H5.9c.2-3 1.2-5 2.1-5zM2.3 7.2h2.4c0-1.8.4-3.3 1-4.3a5.8 5.8 0 0 0-3.4 4.3zm8.9 0h2.5a5.8 5.8 0 0 0-3.4-4.3c.6 1 .9 2.5.9 4.3zM2.3 8.8a5.8 5.8 0 0 0 3.4 4.3c-.6-1-1-2.5-1-4.3zm3.6 0c.2 3 1.2 5 2.1 5s1.9-2 2.1-5zm5.3 0c0 1.8-.3 3.3-.9 4.3a5.8 5.8 0 0 0 3.4-4.3z"/></svg>www.PLUMlearnhub.example</li>
      <li><svg viewBox="0 0 16 16"><path d="M8 0a5 5 0 0 0-5 5c0 4 5 11 5 11s5-7 5-11a5 5 0 0 0-5-5zm0 7a2 2 0 1 1 0-4 2 2 0 0 1 0 4z"/></svg>Suite 140, 82 Orchard Lane Maple Ridge, Alberta</li>
    </ul>
  </section>
</body>
</html>
```